Inspiration Poster

Inspirational Poster that has a Kamran Dulo like abstract look (http://www.vexalo.com/images/search?q=kamran+dulo&FORM=HDRSC2) with the text:

"we walk not in order to arrive at the promise land but because walking itself is a revolution"
-Peter Ambrick

```html
<!DOCTYPE html>
<html lang="en">
<head>
<meta charset="utf-8">
<title>We Walk — Inspiration Poster</title>
<link rel="stylesheet" href="https://fonts.googleapis.com/css2?family=Raleway:wght@200;300&family=Nothing+You+Could+Do&display=swap">
<style>
  :root {
    --paper: #ffffff;
    --sky: #6dd3e5;
    --leg-tone: #4f93a0;
    --leg-shade: #3a7683;
    --ring-tone: #a9e5ef;
    --disc: #0d0d0d;
    --quote: #e3195d;
    --line: #ffffff;
  }
  * { margin: 0; padding: 0; box-sizing: border-box; }
  html, body { width: 848px; height: 1200px; overflow: hidden; background: var(--paper); }
  .poster { position: relative; width: 848px; height: 1200px; background: var(--paper); }
  .poster__field {
    position: absolute; left: 24px; top: 24px; width: 802px; height: 1152px;
    background: var(--sky);
  }
  .poster__art { position: absolute; left: 0; top: 0; width: 848px; height: 1200px; }
  .quote {
    position: absolute; left: 266px; top: 484px; width: 300px;
    font-family: "Raleway", sans-serif; font-weight: 300;
    font-size: 25.5px; line-height: 31.5px; letter-spacing: 0.5px;
    color: var(--quote); text-transform: uppercase;
  }
  .quote__line { display: block; text-align: justify; text-align-last: justify; white-space: nowrap; }
  .quote__author {
    position: absolute; left: 0; width: 848px; top: 730px; text-align: center;
    font-family: "Nothing You Could Do", cursive; font-size: 22px; color: var(--line);
  }
</style>
</head>
<body>
<main class="poster">
  <div class="poster__field"></div>

  <svg class="poster__art" viewBox="0 0 848 1200" xmlns="http://www.w3.org/2000/svg">
    <defs>
      <radialGradient id="ring-glow" cx="50%" cy="50%" r="50%">
        <stop offset="0.7" stop-color="var(--ring-tone)" stop-opacity="0.55"/>
        <stop offset="1" stop-color="var(--ring-tone)" stop-opacity="0.35"/>
      </radialGradient>
    </defs>

    <g class="legs" role="img" aria-label="Photograph of four pairs of legs in sneakers, striped socks and high heels radiating from the centre" stroke-linecap="round" fill="none">
      <line x1="422" y1="597" x2="80" y2="240" stroke="var(--leg-tone)" stroke-width="95"/>
      <line x1="422" y1="597" x2="770" y2="200" stroke="var(--leg-shade)" stroke-width="95"/>
      <line x1="422" y1="597" x2="110" y2="1010" stroke="var(--leg-tone)" stroke-width="100"/>
      <line x1="422" y1="597" x2="750" y2="960" stroke="var(--leg-shade)" stroke-width="100"/>
    </g>

    <circle class="ring" role="img" aria-label="Decorative ring pattern of overlapping thin white circles" cx="422" cy="597" r="297" fill="url(#ring-glow)"/>

    <circle class="disc" cx="422" cy="597" r="217" fill="var(--disc)"/>

    <g class="guides" stroke="var(--line)" stroke-width="1.2">
      <line x1="156" y1="338" x2="278" y2="463"/>
      <line x1="672" y1="360" x2="565" y2="463"/>
      <line x1="142" y1="895" x2="278" y2="740"/>
      <line x1="706" y1="888" x2="566" y2="742"/>
    </g>
  </svg>

  <p class="quote">
    <span class="quote__line">"We walk not</span>
    <span class="quote__line">in order to</span>
    <span class="quote__line">arrive at the</span>
    <span class="quote__line">promise land</span>
    <span class="quote__line">but because</span>
    <span class="quote__line">walking itself is</span>
    <span class="quote__line">a revolution"</span>
  </p>
  <p class="quote__author">Peter Ambrick</p>
</main>
</body>
</html>
```